Brimble Diecast Torvel Collectables Website

looking for a vibrant web site marketplace built for diecast car enthusiasts to buy, sell, and trade with ease. Whether you're looking to showcase your own collection or discover rare and exciting models, our site makes the process simple and enjoyable. Clients can browse a curated inventory of high‑quality diecast cars, connect with fellow collectors, and find the perfect pieces to expand their collection. With a smooth user experience and a community-driven spirit, we’re the go‑to destination for anyone passionate about diecast cars.

Target Market(s)

diecast collectors

Industry/Entity Type

Diecast Collectables

Coding

Coded - Design and coding required

Number of Pages Required

3 page

Font styles to use
Sans Serif

Colors
EE7325
F08F49
F5BC92
FAE3D3
FDF4ED

Requirements
Must have
• Cool look and feel. Woo commerce page to post and sell my inventory
Nice to have
• page for users to post their cars or looking for trades.
Should not have
• look cheap

```html
<!DOCTYPE html>
<html lang="en">
<head>
<meta charset="utf-8">
<title>Brimble Diecast — Buy. Sell. Trade.</title>
<link href="https://fonts.googleapis.com/css2?family=Outfit:wght@500;600;700&family=Inter:wght@400;500;600;700&display=swap" rel="stylesheet">
<style>
:root{
  --orange:#EE7325;
  --orange-2:#F08F49;
  --orange-3:#F5BC92;
  --peach:#FAE3D3;
  --cream:#FDF4ED;
  --ink:#1c1c1c;
  --text:#555;
  --muted:#9a9a9a;
  --line:#ececec;
  --grey-bg:#f4f4f4;
  --dark:#1f1f1f;
}
*{box-sizing:border-box;margin:0;padding:0}
html,body{width:1200px;height:3600px;overflow:hidden}
body{font-family:"Inter",sans-serif;color:var(--ink);background:#fff;font-size:12px}
h1,h2,h3,.display{font-family:"Outfit",sans-serif}
.wrap{width:720px;margin:0 auto;position:relative}
.accent{color:var(--orange)}
.eyebrow{font-size:8.5px;font-weight:600;letter-spacing:1.6px;color:var(--orange);text-transform:uppercase}
.center{text-align:center}
.btn{display:inline-flex;align-items:center;justify-content:center;gap:6px;border-radius:20px;font-weight:600;font-size:11px;height:34px;padding:0 20px}
.btn-solid{background:var(--orange);color:#fff}
.btn-line{border:1.5px solid var(--orange);color:var(--orange)}

/* nav */
.nav{height:42px;display:flex;align-items:center;border-bottom:1px solid var(--line)}
.nav .wrap{display:flex;align-items:center;justify-content:space-between}
.brand{display:flex;align-items:center;gap:7px;font-weight:700;font-size:12px}
.brand-mark{width:18px;height:18px;background:var(--orange);border-radius:3px}
.menu{display:flex;gap:20px;font-size:9.5px;color:#333;margin-left:60px}
.nav-actions{display:flex;gap:8px}
.nav-actions .btn{height:26px;font-size:9px;padding:0 14px}

/* hero */
.hero{height:585px;position:relative;background:linear-gradient(100deg,#141414 0%,#2a2622 45%,#3a332c 70%,#221e1b 100%);color:#fff}
.hero-photo{position:absolute;inset:0;background:radial-gradient(ellipse at 62% 70%,rgba(90,80,70,.55),transparent 55%),linear-gradient(90deg,rgba(10,10,10,.85) 0%,rgba(10,10,10,.35) 55%,rgba(10,10,10,.5) 100%)}
.hero .wrap{padding-top:92px}
.hero-badge{display:inline-block;background:rgba(238,115,37,.18);color:var(--orange-2);font-size:8px;font-weight:600;letter-spacing:1.2px;padding:5px 10px;border-radius:12px}
.hero h1{font-size:40px;line-height:46px;font-weight:600;margin-top:14px}
.hero p{width:300px;font-size:11.5px;line-height:19px;color:#ddd;margin-top:14px}
.hero-ctas{display:flex;gap:10px;margin-top:22px}
.btn-ghost{border:1.5px solid #fff;color:#fff}
.stats{display:flex;gap:16px;margin-top:28px}
.stat{padding-right:16px;border-right:1px solid rgba(255,255,255,.3)}
.stat:last-child{border:0}
.stat b{display:block;font-size:16px;font-weight:600}
.stat span{font-size:8.5px;color:#bbb}

.marquee{height:38px;background:#1b1b1b;display:flex;align-items:center;gap:26px;white-space:nowrap;overflow:hidden;font-size:10px;font-weight:700;letter-spacing:2.2px;color:#8c8c8c;text-transform:uppercase;padding-left:0}
.marquee i{width:4px;height:4px;border-radius:50%;background:var(--orange);display:inline-block}

/* about */
.about{height:445px}
.about .wrap{display:flex;padding-top:70px}
.about-visual{position:relative;width:335px;height:268px;margin-top:22px;background:var(--cream);border-radius:14px;padding:18px;box-shadow:0 6px 20px rgba(0,0,0,.06)}
.about-photo{width:100%;height:100%;border-radius:10px;background:linear-gradient(180deg,#2d3b4c 0%,#4a5866 35%,#6d7378 55%,#3a3a3a 100%)}
.trust{position:absolute;right:-18px;bottom:-12px;background:#fff;border-radius:8px;box-shadow:0 4px 14px rgba(0,0,0,.1);font-size:8.5px;font-weight:600;padding:8px 12px;display:flex;align-items:center;gap:6px}
.about-copy{margin-left:52px;width:333px}
.about-copy h2{font-size:28px;line-height:36px;font-weight:600;margin-top:12px}
.about-copy p{font-size:10px;line-height:19px;color:var(--text);margin-top:14px}
.feature{display:flex;gap:12px;margin-top:16px}
.feature-icon{width:28px;height:28px;border-radius:7px;background:var(--cream);display:flex;align-items:center;justify-content:center;flex:none}
.feature b{font-size:10px;font-weight:600;display:block}
.feature span{font-size:8.5px;color:var(--text)}

/* featured */
.featured{height:598px;background:var(--grey-bg);padding-top:64px}
.featured h2,.how h2,.reviews h2{font-size:28px;font-weight:600;margin-top:12px}
.sub{font-size:11px;color:var(--text);margin-top:12px}
.filters{display:flex;justify-content:center;gap:8px;margin-top:38px}
.chip{height:26px;padding:0 15px;border-radius:14px;background:#fff;border:1px solid #e2e2e2;font-size:8.5px;display:flex;align-items:center}
.chip.on{background:var(--orange);color:#fff;border-color:var(--orange)}
.cards{display:flex;gap:16px;margin-top:18px}
.card{width:168px;height:232px;background:#fff;border-radius:8px;overflow:hidden;box-shadow:0 2px 10px rgba(0,0,0,.05)}
.card-img{height:124px;position:relative}
.tag{position:absolute;left:9px;top:9px;font-size:7px;font-weight:700;color:#fff;padding:3px 7px;border-radius:8px}
.card-body{padding:14px 12px}
.card-body .eyebrow{font-size:7px}
.card-body h3{font-family:"Inter",sans-serif;font-size:10px;font-weight:600;margin-top:7px}
.card-body small{display:block;font-size:7.5px;color:var(--muted);margin-top:6px}
.card-foot{display:flex;justify-content:space-between;align-items:center;margin-top:12px}
.price{font-size:12px;font-weight:700}
.card-foot .btn{height:22px;font-size:8px;padding:0 12px}
.view-all{display:flex;justify-content:center;margin-top:30px}
.view-all .btn{height:36px;width:140px;background:transparent}

/* how */
.how{height:462px;padding-top:64px}
.steps{display:flex;justify-content:space-between;margin-top:60px;position:relative;padding:0 10px}
.step{width:220px;text-align:center;position:relative}
.step-num{font-family:"Outfit",sans-serif;font-size:40px;font-weight:700;color:var(--peach);line-height:40px}
.step-icon{width:38px;height:38px;border-radius:50%;background:var(--cream);margin:8px auto 0;display:flex;align-items:center;justify-content:center}
.step h3{font-family:"Inter",sans-serif;font-size:11px;font-weight:600;margin-top:20px}
.step p{font-size:8.5px;line-height:14px;color:var(--text);margin-top:10px}
.connector{position:absolute;top:36px;width:50px;height:1.5px;background:var(--orange-3)}

/* community */
.community{height:504px;background:var(--grey-bg);padding-top:62px}
.community-card{height:382px;border-radius:14px;background:linear-gradient(120deg,#1e1a18 0%,#2b201a 60%,#4a2a15 100%);display:flex;padding:38px;color:#fff}
.community-copy{width:305px;padding-top:44px}
.community-copy .eyebrow{color:#ddd}
.community-copy h2{font-size:23px;line-height:30px;font-weight:600;margin-top:12px}
.community-copy p{font-size:9.5px;line-height:17px;color:#bbb;margin-top:12px}
.join{display:flex;height:34px;border-radius:18px;background:#fff;color:var(--orange);font-size:10px;font-weight:600;align-items:center;justify-content:center;margin-top:22px}
.members{display:flex;align-items:center;margin-top:16px;font-size:8px;color:#aaa}
.dot{width:20px;height:20px;border-radius:50%;border:2px solid #2b201a;margin-right:-6px;font-size:7px;font-weight:700;display:flex;align-items:center;justify-content:center;color:#fff}
.members span{margin-left:14px}
.gallery{margin-left:auto;display:grid;grid-template-columns:150px 150px;gap:8px;align-content:start;margin-top:-10px}
.shot{height:143px;background:rgba(255,255,255,.07);border-radius:8px;padding:8px}
.shot-img{height:98px;border-radius:6px}
.shot span{display:block;font-size:8px;color:#ccc;margin-top:10px}

/* reviews */
.reviews{height:385px;padding-top:64px}
.review-row{display:flex;gap:18px;margin-top:40px}
.review{width:228px;height:166px;border:1px solid var(--line);border-radius:10px;padding:20px}
.stars{color:var(--orange);font-size:10px;letter-spacing:2px}
.review q{display:block;font-size:9px;line-height:16px;color:var(--text);font-style:italic;margin-top:10px;height:66px}
.who{display:flex;align-items:center;gap:9px;margin-top:10px}
.avatar{width:22px;height:22px;border-radius:50%;background:linear-gradient(135deg,var(--orange-3),#8a6a55)}
.who b{font-size:9px;font-weight:600;display:block}
.who span{font-size:7.5px;color:var(--muted)}

/* newsletter */
.newsletter{height:319px;background:var(--cream);padding-top:60px}
.news-card{height:198px;background:#fff;border-radius:14px;display:flex;align-items:center;padding:0 38px;box-shadow:0 4px 16px rgba(0,0,0,.04)}
.news-card h2{font-size:19px;font-weight:600}
.news-card p{font-size:9.5px;color:var(--text);margin-top:12px}
.sub-form{display:flex;gap:6px;margin-top:20px}
.field{width:322px;height:32px;border:1px solid #ddd;border-radius:17px;font-size:9px;color:var(--muted);display:flex;align-items:center;padding-left:14px}
.sub-form .btn{height:32px;font-size:9px;width:98px}
.news-photo{margin-left:52px;width:96px;height:96px;border-radius:50%;border:4px solid var(--peach);background:radial-gradient(circle at 45% 55%,#7aa6c9,#2a4a6a 70%)}

/* footer */
.footer{height:220px;background:var(--dark);color:#aaa;padding-top:46px}
.footer-top{display:flex}
.footer-brand{width:240px}
.footer-brand .brand{color:#fff}
.footer-brand p{font-size:8.5px;line-height:15px;margin-top:14px}
.socials{display:flex;gap:8px;margin-top:12px}
.socials i{width:20px;height:20px;border-radius:50%;border:1px solid #555;display:block}
.footer-col{width:168px}
.footer-col h4{font-size:9.5px;color:#fff;font-weight:600;margin-bottom:14px}
.footer-col a{display:block;font-size:8.5px;color:#999;margin-bottom:11px;text-decoration:none}
.footer-bottom{display:flex;justify-content:space-between;font-size:7.5px;color:#777;border-top:1px solid #333;margin-top:20px;padding-top:14px}
</style>
</head>
<body>

<header class="nav">
  <div class="wrap">
    <div class="brand"><span class="brand-mark"></span>Brimble Diecast</div>
    <nav class="menu"><span>Home</span><span>About</span><span>Collection</span><span>How It Works</span><span>Community</span><span>Contact</span></nav>
    <div class="nav-actions"><span class="btn btn-line">Browse</span><span class="btn btn-solid">Start Selling</span></div>
  </div>
</header>

<section class="hero">
  <div class="hero-photo" role="img" aria-label="Dark moody photo of a classic sports car on a city street"></div>
  <div class="wrap">
    <span class="hero-badge">THE #1 DIECAST MARKETPLACE</span>
    <h1>Buy. Sell. Trade.<br><span class="accent">Miniature<br>Masterpieces.</span></h1>
    <p>The ultimate hub for diecast collectors. Explore a growing marketplace where you can buy, sell, or trade your favorite models with collectors from around the world.</p>
    <div class="hero-ctas">
      <span class="btn btn-solid">Explore Collection
        <svg width="10" height="10" viewBox="0 0 10 10"><path d="M1 5h8M6 2l3 3-3 3" stroke="#fff" stroke-width="1.4" fill="none"/></svg></span>
      <span class="btn btn-ghost">How It Works</span>
    </div>
    <div class="stats">
      <div class="stat"><b>2,500+</b><span>Models Listed</span></div>
      <div class="stat"><b>1,200+</b><span>Collectors</span></div>
      <div class="stat"><b>98%</b><span>Satisfaction</span></div>
    </div>
  </div>
</section>

<div class="marquee">
  <span>Blaze Rollers</span><i></i><span>Crate Minis</span><i></i><span>Vantor</span><i></i><span>Brezzia</span><i></i><span>Apex Scale</span><i></i><span>Signal Works</span><i></i><span>Kestrel Machines</span><i></i><span>Bolt Street</span><i></i><span>Blaze Rollers</span><i></i><span>Crate Minis</span>
</div>

<section class="about">
  <div class="wrap">
    <div class="about-visual">
      <div class="about-photo" role="img" aria-label="Photo of sports cars lined up on a racetrack"></div>
      <div class="trust">
        <svg width="12" height="12" viewBox="0 0 24 24"><path d="M12 2l3 7 7 .6-5.3 4.7 1.6 7.2L12 17.8 5.7 21.5l1.6-7.2L2 9.6 9 9z" fill="none" stroke="#EE7325" stroke-width="2"/></svg>
        Trusted by 1,200+ Collectors
      </div>
    </div>
    <div class="about-copy">
      <div class="eyebrow">About Us</div>
      <h2>We Bring Collectors<br><span class="accent">Together</span></h2>
      <p>We bring together passionate collectors and high-quality diecast cars in one trusted space. Whether you're hunting for rare finds or looking to give your collection a new home, our platform makes every transaction smooth and secure.</p>
      <div class="feature">
        <div class="feature-icon"><svg width="13" height="13" viewBox="0 0 24 24"><path d="M12 3l8 3v6c0 5-4 8-8 9-4-1-8-4-8-9V6z" fill="none" stroke="#EE7325" stroke-width="2"/></svg></div>
        <div><b>Verified Listings</b><span>Every model is inspected for quality and photographed clearly.</span></div>
      </div>
      <div class="feature">
        <div class="feature-icon"><svg width="13" height="13" viewBox="0 0 24 24"><circle cx="9" cy="8" r="4" fill="none" stroke="#EE7325" stroke-width="2"/><path d="M2 21c0-4 3-6 7-6s7 2 7 6M16 4a4 4 0 010 8M22 21c0-3-2-5-4-6" fill="none" stroke="#EE7325" stroke-width="2"/></svg></div>
        <div><b>Community Driven</b><span>Connect, trade, and share with fellow enthusiasts worldwide.</span></div>
      </div>
      <div class="feature">
        <div class="feature-icon"><svg width="13" height="13" viewBox="0 0 24 24"><rect x="2" y="5" width="20" height="14" rx="2" fill="none" stroke="#EE7325" stroke-width="2"/><path d="M2 10h20" stroke="#EE7325" stroke-width="2"/></svg></div>
        <div><b>Secure Transactions</b><span>Safe payments and buyer protection on every deal.</span></div>
      </div>
    </div>
  </div>
</section>

<section class="featured">
  <div class="wrap center">
    <div class="eyebrow">Featured Collection</div>
    <h2>Discover Rare &amp; <span class="accent">Exclusive Models</span></h2>
    <p class="sub">Curated picks from our top sellers. Each piece tells a story.</p>
    <div class="filters">
      <span class="chip on">All</span><span class="chip">Vintage</span><span class="chip">Muscle Cars</span><span class="chip">Exotics</span><span class="chip">Trucks &amp; SUVs</span>
    </div>
    <div class="cards" style="text-align:left">
      <article class="card">
        <div class="card-img" role="img" aria-label="Photo of an orange classic muscle car model" style="background:linear-gradient(160deg,#f0b070,#c8642a 55%,#6a3a20)"><span class="tag" style="background:var(--orange)">HOT</span></div>
        <div class="card-body"><div class="eyebrow">Blaze Rollers</div><h3>1969 Stallion R/T</h3><small>1:18 Scale • Mint Condition</small>
          <div class="card-foot"><span class="price">$89.99</span><span class="btn btn-solid">Add to Cart</span></div></div>
      </article>
      <article class="card">
        <div class="card-img" role="img" aria-label="Photo of a black exotic supercar model" style="background:linear-gradient(160deg,#5a4a40,#2a2a2e 55%,#141416)"><span class="tag" style="background:#8b5cf6">RARE</span></div>
        <div class="card-body"><div class="eyebrow">Apex Scale</div><h3>Veloce Aurora SV</h3><small>1:18 Scale • Limited Edition</small>
          <div class="card-foot"><span class="price">$249.99</span><span class="btn btn-solid">Add to Cart</span></div></div>
      </article>
      <article class="card">
        <div class="card-img" role="img" aria-label="Photo of a red vintage sedan model on a street" style="background:linear-gradient(160deg,#8a8076,#b4552e 55%,#4a3a30)"></div>
        <div class="card-body"><div class="eyebrow">Crate Minis</div><h3>1957 Harbor Cruiser</h3><small>1:24 Scale • Excellent</small>
          <div class="card-foot"><span class="price">$64.99</span><span class="btn btn-solid">Add to Cart</span></div></div>
      </article>
      <article class="card">
        <div class="card-img" role="img" aria-label="Photo of a white pickup truck model" style="background:linear-gradient(160deg,#9aa6b2,#d8dadc 55%,#5a6068)"><span class="tag" style="background:#2e9a4a">NEW</span></div>
        <div class="card-body"><div class="eyebrow">Signal Works</div><h3>Summit T-150 Trail 2023</h3><small>1:24 Scale • Brand New</small>
          <div class="card-foot"><span class="price">$54.99</span><span class="btn btn-solid">Add to Cart</span></div></div>
      </article>
    </div>
    <div class="view-all"><span class="btn btn-line">View Full Collection</span></div>
  </div>
</section>

<section class="how">
  <div class="wrap center">
    <div class="eyebrow">How It Works</div>
    <h2>Three Simple <span class="accent">Steps</span></h2>
    <p class="sub">Getting started is easy — whether you're buying or selling.</p>
    <div class="steps">
      <div class="step">
        <div class="step-num">01</div>
        <div class="step-icon"><svg width="15" height="15" viewBox="0 0 24 24"><circle cx="11" cy="11" r="7" fill="none" stroke="#EE7325" stroke-width="2"/><path d="M16 16l5 5" stroke="#EE7325" stroke-width="2"/></svg></div>
        <h3>Browse or List</h3>
        <p>Explore our curated collection or list<br>your own diecast cars in minutes<br>with our simple selling tools.</p>
      </div>
      <span class="connector" style="left:238px"></span>
      <div class="step">
        <div class="step-num">02</div>
        <div class="step-icon"><svg width="15" height="15" viewBox="0 0 24 24"><path d="M4 4h16v12H8l-4 4z" fill="none" stroke="#EE7325" stroke-width="2" stroke-linejoin="round"/></svg></div>
        <h3>Connect &amp; Negotiate</h3>
        <p>Chat directly with sellers or buyers.<br>Make offers, arrange trades, and find<br>your perfect match.</p>
      </div>
      <span class="connector" style="left:478px"></span>
      <div class="step">
        <div class="step-num">03</div>
        <div class="step-icon"><svg width="15" height="15" viewBox="0 0 24 24"><circle cx="12" cy="12" r="9" fill="none" stroke="#EE7325" stroke-width="2"/><path d="M8 12l3 3 6-6" fill="none" stroke="#EE7325" stroke-width="2"/></svg></div>
        <h3>Complete the Deal</h3>
        <p>Secure checkout with buyer<br>protection. Your new piece ships<br>safely to your doorstep.</p>
      </div>
    </div>
  </div>
</section>

<section class="community">
  <div class="wrap">
    <div class="community-card">
      <div class="community-copy">
        <div class="eyebrow">Join the Community</div>
        <h2>Show Off Your Collection.<br>Discover New Treasures.</h2>
        <p>Join a community of diecast enthusiasts who share your passion. Post your collection, discuss rare finds, and stay updated on new releases.</p>
        <div class="join">Join Now — It's Free</div>
        <div class="members">
          <span class="dot" style="background:#EE7325">D</span><span class="dot" style="background:#F08F49">M</span><span class="dot" style="background:#F5BC92">K</span><span class="dot" style="background:#c86a30">R</span>
          <span>+1,200 collectors</span>
        </div>
      </div>
      <div class="gallery">
        <div class="shot"><div class="shot-img" role="img" aria-label="Photo of a blue sports coupe model on a coastal road" style="background:linear-gradient(160deg,#7fb0d8,#2f6aa0 60%,#5a6a70)"></div><span>Vauss GT3 Coupe</span></div>
        <div class="shot"><div class="shot-img" role="img" aria-label="Photo of a red classic grand tourer model in a street" style="background:linear-gradient(160deg,#6a5a50,#c8432a 60%,#3a2a22)"></div><span>Rossa 250 GT</span></div>
        <div class="shot"><div class="shot-img" role="img" aria-label="Photo of an orange formula race car model" style="background:linear-gradient(160deg,#b0b8c0,#d8642a 55%,#3a3a3a)"></div><span>Kessler Formula Racer</span></div>
        <div class="shot"><div class="shot-img" role="img" aria-label="Photo of a light blue sports car model" style="background:linear-gradient(160deg,#c8dceb,#5a9acb 60%,#2a4a6a)"></div><span>Kaito Sprint MK4</span></div>
      </div>
    </div>
  </div>
</section>

<section class="reviews">
  <div class="wrap center">
    <div class="eyebrow">What Collectors Say</div>
    <h2>Loved by <span class="accent">Enthusiasts</span></h2>
    <div class="review-row" style="text-align:left">
      <div class="review"><div class="stars">★★★★★</div>
        <q>"Found a rare '67 fastback I'd been hunting for years. The seller was verified and the condition was exactly as described. Couldn't be happier!"</q>
        <div class="who"><span class="avatar" role="img" aria-label="Collector portrait"></span><div><b>Jake Morrison</b><span>Collector since 2015</span></div></div></div>
      <div class="review"><div class="stars">★★★★★</div>
        <q>"I sold over 30 models in my first month. The listing process is incredibly simple and the community is so supportive. Best platform out there."</q>
        <div class="who"><span class="avatar" role="img" aria-label="Seller portrait"></span><div><b>Sarah Chen</b><span>Seller &amp; Collector</span></div></div></div>
      <div class="review"><div class="stars">★★★★★</div>
        <q>"The trade feature is a game changer. Swapped duplicates for models I actually wanted. It's like being at a car meet, but online!"</q>
        <div class="who"><span class="avatar" role="img" aria-label="Trader portrait"></span><div><b>Ryan Patel</b><span>Trading enthusiast</span></div></div></div>
    </div>
  </div>
</section>

<section class="newsletter">
  <div class="wrap">
    <div class="news-card">
      <div>
        <h2>Stay in the Loop</h2>
        <p>Get notified about rare drops, new listings, and collector tips. No spam, ever.</p>
        <div class="sub-form"><span class="field">Enter your email</span><span class="btn btn-solid">Subscribe</span></div>
      </div>
      <div class="news-photo" role="img" aria-label="Photo of a blue sports car model"></div>
    </div>
  </div>
</section>

<footer class="footer">
  <div class="wrap">
    <div class="footer-top">
      <div class="footer-brand">
        <div class="brand"><span class="brand-mark"></span>Brimble Diecast</div>
        <p>The ultimate marketplace for diecast car<br>collectors. Buy, sell, and trade with confidence.</p>
        <div class="socials"><i></i><i></i><i></i><i></i></div>
      </div>
      <div class="footer-col"><h4>Marketplace</h4><a>Browse Cars</a><a>Sell Your Collection</a><a>Trade Center</a><a>New Arrivals</a></div>
      <div class="footer-col"><h4>Company</h4><a>About Us</a><a>Contact</a><a>Blog</a><a>Careers</a></div>
      <div class="footer-col"><h4>Support</h4><a>Help Center</a><a>Shipping Info</a><a>Returns</a><a>Privacy Policy</a></div>
    </div>
    <div class="footer-bottom"><span>© 2026 Brimble Diecast. All rights reserved.</span><span>Where Collectors Connect</span></div>
  </div>
</footer>

</body>
</html>
```